Mental Health Services for Employees - we need a website for our new business

We need a simple web design to showcase our various services. Our programs help organizations to ensure the heath and wellness of their workers. Our company is called "Brightway Workplace Partners Inc." or "Brightway" We'd like to see designs that use the colour palette from our logo. Our customers our fairly conservative, and our design should communicate due diligence around providing a safe and healthy environment for workers. Attached our the logo files. Also sample photographs from our purchased images - others available. Original design for website is found here: https://lanternow7.examplesite.com/mypage-1 A key page not listed in our original design is a section that lists "Five Reasons to Work With Us". We will need to be able to modify and change the copy/menu options as the business grows.

Target Market(s)

businesses who want to provide health and wellness services for their employees

Coding

Coded - Design and coding required

Number of Pages Required

2 page

Font styles to use
Sans Serif

Requirements
Must have
• colours that work with our attached logo

```html
<!DOCTYPE html>
<html lang="en">
<head>
<meta charset="utf-8">
<title>Brightway Workplace Partners Inc.</title>
<link href="https://fonts.googleapis.com/css2?family=Roboto:ital,wght@0,300;0,400;0,500;0,700;1,400&family=Roboto+Condensed:wght@400;700&display=swap" rel="stylesheet">
<style>
:root{
  --teal:#16a085;
  --teal-light:#2bbfa4;
  --teal-dark:#0f7a66;
  --ink:#2b2b2b;
  --body:#6a6a6a;
  --muted:#9a9a9a;
  --line:#e3e3e3;
  --soft:#f5f6f6;
  --footer:#232323;
  --footer-deep:#1a1a1a;
  --amber:#f2c230;
  --white:#ffffff;
}
*{box-sizing:border-box;margin:0;padding:0}
html,body{width:1200px;height:4286px;overflow:hidden}
body{font-family:"Roboto",sans-serif;color:var(--body);background:var(--white);font-size:15px;line-height:1.6}
h1,h2,h3,h4{font-family:"Roboto Condensed",sans-serif;color:var(--ink);font-weight:700}
.wrap{width:860px;margin:0 auto;position:relative}

/* header + hero */
.hero{position:relative;height:565px;overflow:hidden}
.hero-photo{position:absolute;inset:0;background:linear-gradient(180deg,#2f6f63 0%,#6e8a5a 35%,#b89a55 65%,#d8b56e 100%)}
.hero-tint{position:absolute;inset:0;background:linear-gradient(180deg,rgba(14,90,78,.75) 0%,rgba(22,120,100,.35) 45%,rgba(0,0,0,0) 100%)}
.topbar{position:absolute;top:0;left:0;right:0;height:95px;display:flex;align-items:center;padding:0 170px}
.brand{display:flex;align-items:center;gap:10px;color:var(--white);font-family:"Roboto Condensed",sans-serif;font-weight:700;font-size:22px;letter-spacing:.5px;line-height:1.1}
.brand-mark{width:30px;height:30px;background:var(--teal-light);flex:none}
.nav{display:flex;gap:22px;margin-left:40px;list-style:none}
.nav li{color:var(--white);font-size:12px;font-weight:500;text-transform:uppercase;letter-spacing:.6px}
.phone{margin-left:auto;text-align:right;color:var(--teal-light);font-family:"Roboto Condensed",sans-serif;font-weight:700;font-size:26px;line-height:1}
.phone small{display:block;color:var(--white);font-family:"Roboto",sans-serif;font-size:11px;font-weight:400;margin-top:4px}
.hero-frame{position:absolute;left:220px;top:148px;width:550px;height:345px;border:2px solid rgba(255,255,255,.9);border-right:none;padding:70px 40px 0 34px}
.hero-frame h1{color:var(--white);font-size:34px;line-height:1.2;text-transform:uppercase;letter-spacing:.5px}
.hero-frame p{color:#f1f1f1;font-size:15px;margin-top:26px;max-width:380px}
.hero-corner{position:absolute;right:-2px;bottom:-2px}

/* about */
.about{position:relative;height:615px}
.about-text{position:absolute;left:170px;top:110px;width:470px}
.about-text h2{font-size:27px;margin-bottom:18px}
.about-text p{font-size:14px;margin-bottom:22px}
.about-photo{position:absolute;left:680px;top:-22px;width:375px;height:528px;background:linear-gradient(135deg,#6f8fa6 0%,#a9b7c2 40%,#e0a030 70%,#3b4a58 100%)}
.about-tab{position:absolute;left:652px;top:42px;width:28px;height:80px;background:var(--teal)}

/* services */
.services{background:var(--soft);height:625px;padding-top:58px}
.services-head{display:flex;gap:70px;align-items:flex-start}
.services-head h2{font-size:27px;text-transform:uppercase;width:300px;padding-top:6px}
.services-head p{font-size:17px;color:var(--ink);line-height:1.45;width:490px}
.service-grid{display:grid;grid-template-columns:repeat(3,1fr);gap:30px;margin-top:50px}
.service-photo{height:270px;border-top:8px solid var(--teal)}
.service-card h3{font-size:21px;text-transform:uppercase;text-align:center;margin-top:22px}
.service-card p{font-size:12.5px;text-align:center;line-height:1.5;margin-top:6px;padding:0 14px}

/* why */
.why{height:515px;padding-top:70px;text-align:center}
.why h2{font-size:28px}
.why-intro{width:720px;margin:18px auto 0;font-size:14.5px}
.reasons{display:flex;justify-content:center;gap:62px;margin-top:52px;list-style:none}
.reason{width:120px;display:flex;flex-direction:column;align-items:center}
.reason-icon{width:64px;height:64px;border:2px solid var(--teal);border-radius:50%;display:flex;align-items:center;justify-content:center}
.reason span{font-family:"Roboto Condensed",sans-serif;color:var(--ink);font-size:15px;font-weight:700;margin-top:18px}

/* news */
.news{background:var(--soft);height:820px;padding-top:58px;text-align:center}
.news h2{font-size:30px}
.news-grid{display:grid;grid-template-columns:repeat(3,1fr);gap:28px;margin-top:52px;text-align:left}
.news-card{background:var(--white);box-shadow:0 2px 8px rgba(0,0,0,.06)}
.news-photo{height:215px;position:relative}
.news-date{position:absolute;left:0;bottom:-14px;background:var(--teal);color:var(--white);font-size:11px;padding:5px 12px;display:flex;gap:18px}
.news-body{padding:30px 18px 20px}
.news-body h3{font-size:18px;line-height:1.25}
.news-body p{font-size:12.5px;line-height:1.55;margin-top:12px}
.news-more{display:block;text-align:right;color:var(--teal);font-size:13px;margin-top:16px}
.btn{display:inline-block;background:var(--teal);color:var(--white);font-size:14px;font-weight:500;border:none;padding:14px 38px;font-family:"Roboto",sans-serif}
.news .btn{margin-top:34px}

/* testimonial */
.testimonial{height:485px;text-align:center;padding-top:68px}
.testimonial h2{font-size:28px}
.quote-mark{color:#c8c8c8;font-size:54px;font-family:Georgia,serif;line-height:1;margin-top:22px;height:40px}
.testimonial blockquote{width:870px;margin:14px auto 0;font-style:italic;font-size:15px;line-height:1.75;color:var(--body)}
.person{display:flex;align-items:center;justify-content:center;gap:16px;margin-top:40px}
.avatar{width:64px;height:64px;border-radius:50%;background:linear-gradient(135deg,#c99a78,#8a6148)}
.person b{font-family:"Roboto Condensed",sans-serif;color:var(--ink);font-size:17px}

/* contact */
.contact{position:relative;height:445px;overflow:hidden}
.contact-photo{position:absolute;inset:0;background:linear-gradient(90deg,#d6b28c 0%,#b7946f 25%,#7a8f82 45%,#2a9c86 62%,#16a085 100%)}
.contact-form{position:absolute;left:600px;top:60px;width:430px}
.contact-form h2{color:var(--white);font-size:30px}
.contact-form .lead{color:#e8f6f2;font-size:14px;margin:4px 0 16px}
.row{display:flex;gap:12px;margin-bottom:12px}
.field{flex:1;height:34px;background:var(--white);font-size:12px;color:var(--muted);padding:8px 12px}
.field.tall{height:110px}
.consent{display:flex;gap:8px;align-items:flex-start;color:#e8f6f2;font-size:11px;line-height:1.4;margin:4px 0 14px}
.box{width:12px;height:12px;border:1px solid var(--white);flex:none;margin-top:1px}
.contact-form .btn{width:100%;background:var(--teal-dark);font-size:12px;letter-spacing:.8px;padding:11px}

/* footer */
.footer{background:var(--footer);height:181px;padding-top:32px;color:#b8b8b8;font-size:12px;line-height:1.55}
.footer-grid{display:grid;grid-template-columns:230px 190px 210px 1fr;gap:22px}
.footer .brand{font-size:17px;margin-bottom:10px}
.footer .brand-mark{width:22px;height:22px}
.footer h4{color:var(--teal-light);font-size:17px;margin-bottom:8px}
.footer ul{list-style:none}
.footer li{padding-left:12px;position:relative}
.footer li::before{content:"";position:absolute;left:0;top:7px;width:4px;height:4px;background:var(--teal-light)}
.contact-line{display:flex;gap:8px;align-items:flex-start;margin-bottom:3px}
.socials{display:flex;gap:8px;margin-top:6px}
.socials i{width:22px;height:22px;border:1px solid #888;border-radius:50%}
.sub-field{height:30px;background:var(--white);color:var(--muted);padding:6px 10px;margin-top:8px}
.footer .btn{margin-top:8px;font-size:11px;padding:7px 26px;letter-spacing:.6px}
.copyright{background:var(--footer-deep);height:36px;color:#9a9a9a;font-size:11px;text-align:center;line-height:36px}
</style>
</head>
<body>

<header class="hero">
  <div class="hero-photo" role="img" aria-label="Mining trucks working on a dusty open-pit site at dusk"></div>
  <div class="hero-tint"></div>
  <div class="topbar">
    <div class="brand"><span class="brand-mark"></span>Brightway</div>
    <ul class="nav"><li>Home</li><li>Services</li><li>About</li><li>SAP</li><li>Referrals</li><li>Contact</li></ul>
    <div class="phone">888-555-0142<small>hello@brightwayworkplace.example</small></div>
  </div>
  <div class="hero-frame">
    <h1>Helping organizations maintain<br>a safe workplace</h1>
    <p>Brightway is ready to provide organizations with access to a suite of best practice solutions and options for your employees.</p>
    <svg class="hero-corner" width="46" height="46" viewBox="0 0 46 46"><polygon points="46,0 46,46 0,46" fill="var(--amber)"/></svg>
  </div>
</header>

<section class="about">
  <div class="about-text">
    <h2>About Brightway Workplace Partners Inc</h2>
    <p>Brightway Workplace Partners Inc. ("Brightway") provides outstanding business-to-business services that support and promote health, wellness, and safety in the workplace. Brightway's flagship programs are the Substance Abuse Professional (SAP) and Specialized Addiction Case Management services.</p>
    <p>Brightway is ready to provide organizations with access to a suite of best practice solutions and options for your employees. These services empower organizations to effectively deal with substance use, to understand and fulfil various legislative and/or policy requirements, and to help keep their workers safe and healthy.</p>
    <p>Whenever organizations have a need to address substance use in the workplace please consider us a resource to help with program development based on the locations and specific needs of your employees.</p>
  </div>
  <div class="about-tab"></div>
  <div class="about-photo" role="img" aria-label="Gloved worker in safety gear handling an orange railing"></div>
</section>

<section class="services">
  <div class="wrap">
    <div class="services-head">
      <h2>Our Services</h2>
      <p>These services empower organizations to effectively deal with substance use, to understand and fulfil various legislative and/or policy requirements, and to help keep their workers safe and healthy</p>
    </div>
    <div class="service-grid">
      <article class="service-card">
        <div class="service-photo" role="img" aria-label="Workers in hard hats and safety vests on site" style="background:linear-gradient(135deg,#e0b84a,#c7c9a2 50%,#7d9c9a)"></div>
        <h3>Accommodation Screening</h3>
        <p>Rapid screening helps employers learn what support a worker needs and how to provide accommodation.</p>
      </article>
      <article class="service-card">
        <div class="service-photo" role="img" aria-label="Two people talking during a counselling session" style="background:linear-gradient(135deg,#e9ecef,#c9ced3 55%,#a6b0b8)"></div>
        <h3>SAP Assessments</h3>
        <p>Our trained SAP is experts at assessing an organization's workers and developing solutions that will protect them.</p>
      </article>
      <article class="service-card">
        <div class="service-photo" role="img" aria-label="Silhouetted workers beside an oil pump at sunset" style="background:linear-gradient(180deg,#a9c3d6,#d9c7a5 60%,#2f3a40)"></div>
        <h3>SACM</h3>
        <p>This is a unique and specialized program offered by Brightway that focuses on the needs of individuals struggling with addiction.</p>
      </article>
    </div>
  </div>
</section>

<section class="why">
  <h2>Why Work With Us</h2>
  <p class="why-intro">Brightway Workplace Partners Inc. ("Brightway") provides outstanding business-to-business services that support and promote health, wellness, and safety in the workplace. Brightway's flagship programs are the Substance Abuse Professional (SAP) and Specialized Addiction Case Management services.</p>
  <ul class="reasons">
    <li class="reason"><div class="reason-icon"><svg width="30" height="30" viewBox="0 0 30 30" fill="none" stroke="var(--teal)" stroke-width="2"><rect x="6" y="4" width="18" height="22" rx="2"/><path d="M10 11h10M10 16h10M10 21h6"/></svg></div><span>SAP Assessment</span></li>
    <li class="reason"><div class="reason-icon"><svg width="30" height="30" viewBox="0 0 30 30" fill="none" stroke="var(--teal)" stroke-width="2"><path d="M4 14l11-9 11 9M7 12v13h16V12"/><path d="M12 25v-7h6v7"/></svg></div><span>Accommodation</span></li>
    <li class="reason"><div class="reason-icon"><svg width="30" height="30" viewBox="0 0 30 30" fill="none" stroke="var(--teal)" stroke-width="2"><circle cx="15" cy="15" r="10"/><path d="M10 15l4 4 7-8"/></svg></div><span>Specialized Program</span></li>
    <li class="reason"><div class="reason-icon"><svg width="30" height="30" viewBox="0 0 30 30" fill="none" stroke="var(--teal)" stroke-width="2"><path d="M5 20c4-10 16-10 20 0"/><path d="M21 13l4 7-7 1"/></svg></div><span>Flexibility</span></li>
    <li class="reason"><div class="reason-icon"><svg width="30" height="30" viewBox="0 0 30 30" fill="none" stroke="var(--teal)" stroke-width="2"><path d="M15 4l3 7 7 1-5 5 1 8-6-4-6 4 1-8-5-5 7-1z"/></svg></div><span>Motivation</span></li>
  </ul>
</section>

<section class="news">
  <h2>Latest News</h2>
  <div class="wrap">
    <div class="news-grid">
      <article class="news-card">
        <div class="news-photo" role="img" aria-label="Worker in orange coveralls and hard hat" style="background:linear-gradient(135deg,#e7e3dc,#e0763a 55%,#6a6a6a)"><div class="news-date"><span>Oct 18, 2019</span><span>Safety Tips</span></div></div>
        <div class="news-body"><h3>Mental Health Affects Three Out of Four U.S. Workers</h3><p>A new survey finds that most employees feel mental health issues affect their work, leaving many unsure where to turn for help.</p><a class="news-more">Continue &rarr;</a></div>
      </article>
      <article class="news-card">
        <div class="news-photo" role="img" aria-label="Person sitting thoughtfully in a bright office" style="background:linear-gradient(135deg,#f1efec,#cdbfae 60%,#9c8a78)"><div class="news-date"><span>Sep 24, 2019</span><span>Mental Health</span></div></div>
        <div class="news-body"><h3>It's not as easy conversation - Mental health in the workplace</h3><p>Talking openly about mental health at work can be hard, yet early support helps employees recover and return stronger.</p><a class="news-more">Continue &rarr;</a></div>
      </article>
      <article class="news-card">
        <div class="news-photo" role="img" aria-label="Construction crew in safety gear on a work site" style="background:linear-gradient(135deg,#c64a3a,#d99a6a 50%,#8c8f93)"><div class="news-date"><span>Aug 30, 2019</span><span>Workplace</span></div></div>
        <div class="news-body"><h3>U.S. Worker Depression Rates Skyrocket</h3><p>Reported rates of depression among workers have climbed sharply, pushing employers to rethink their wellness plans.</p><a class="news-more">Continue &rarr;</a></div>
      </article>
    </div>
  </div>
  <span class="btn">Load More</span>
</section>

<section class="testimonial">
  <h2>Testimonial</h2>
  <div class="quote-mark">&ldquo;</div>
  <blockquote>Working with Brightway gave our managers clear steps for supporting staff through difficult times. The team was responsive, thorough and respectful, and our workers felt truly cared for. We now have a program that protects people and keeps our sites safe, and we would recommend them to any employer who values wellbeing.</blockquote>
  <div class="person"><div class="avatar" role="img" aria-label="Portrait of the client"></div><b>Dana Whitfield</b></div>
</section>

<section class="contact">
  <div class="contact-photo" role="img" aria-label="Woman speaking with a counsellor in a calm room"></div>
  <div class="contact-form">
    <h2>Fill out the following form</h2>
    <p class="lead">Your request will be answered within 24 hours</p>
    <div class="row"><div class="field">Name</div><div class="field">E-mail</div></div>
    <div class="row"><div class="field">Subject</div></div>
    <div class="row"><div class="field tall">Message</div></div>
    <div class="consent"><span class="box"></span>I agree to have my information stored so the team can follow up on my request.</div>
    <span class="btn">SEND MESSAGE</span>
  </div>
</section>

<footer class="footer">
  <div class="wrap footer-grid">
    <div>
      <div class="brand"><span class="brand-mark"></span>Brightway</div>
      <p>Brightway Workplace Partners Inc. provides outstanding business services that support and promote health, wellness, and safety in the workplace.</p>
    </div>
    <div>
      <h4>Services</h4>
      <ul><li>Accommodation Screening</li><li>SAP Assessments</li><li>Specialized Addiction Case Management</li></ul>
    </div>
    <div>
      <h4>Stay with us</h4>
      <div class="contact-line"><svg width="12" height="14" viewBox="0 0 12 14"><path d="M6 1a4.5 4.5 0 0 0-4.5 4.5C1.5 9 6 13 6 13s4.5-4 4.5-7.5A4.5 4.5 0 0 0 6 1z" fill="var(--teal-light)"/></svg><span>48 Harbor Lane, Suite 210<br>Lakeview ON L2K 4P7</span></div>
      <div class="contact-line"><svg width="12" height="12" viewBox="0 0 12 12"><path d="M2 1h3l1 3-2 1a7 7 0 0 0 3 3l1-2 3 1v3c-6 1-10-3-9-9z" fill="var(--teal-light)"/></svg><span>888-555-0142</span></div>
      <div class="contact-line"><svg width="12" height="10" viewBox="0 0 12 10"><rect x=".5" y=".5" width="11" height="9" fill="none" stroke="var(--teal-light)"/><path d="M.5.5L6 5l5.5-4.5" fill="none" stroke="var(--teal-light)"/></svg><span>hello@brightwayworkplace.example</span></div>
      <div class="socials"><i></i><i></i><i></i></div>
    </div>
    <div>
      <h4>Subscribe</h4>
      <p>Subscribe to our mailing list to get the updates to your email inbox.</p>
      <div class="sub-field">Email address</div>
      <span class="btn">SUBSCRIBE</span>
    </div>
  </div>
</footer>
<div class="copyright">Copyright &copy; 2019 Brightway. All Rights Reserved</div>

</body>
</html>
```